Sassy, natural personal lubricant knows that it is not always about the packaging

An opportunity exists to create packaging for the world's first Macadamia Oil personal lubricant - Worrabee Silk. Unlike any other personal lubricants, this product is created from pure macadamia nut oil. The fatty acids naturally occurring in Macadamia oil are highly anti-inflammatory and are the closest in composition to human skin lipids. Using Worrabee Silk in such a vulnerable part of our bodies is the safest and gentlest way to enhance sexual enjoyment while moisturizing and adding lubrication. Worrabee Silk is completely free of the parabens, glycerins, fragrances, hormones, silicones and petroleum products known to irritate the delicate vaginal wall.

Design tone for Worrabee Silk:
- intelligent, but not condescending or patronizing
- elegant and dignified but not prudish
- clean, natural, uninhibited

Design specs:
- See attached file for packaging specs

Colors:
- refer to www.worrabee-example.com to see other products in the range. This is a guide only. Use of those colors is not mandatory.

Ingredients:

100% Macadamia Oil

Additional features:

- edible
- vegan
- gluten-free
- low allergen
- naturally anti-microbial and anti-inflammatory

See http://thebarebotanist-example.com/benefits-of-macadamia-nut-oil-in-skin-care/ for a list of the benefits of macadamia oil.

Target Market(s)

Our target market are the early adopters within the baby boomer set. Their age is a badge of honor, they are comfortable in their own skin and as sensual and fun-loving as ever. They are in their prime - still cool, still curious, still a little crazy. They are open to new possibilities, just as they have been at every age and stage. They still have plenty to do and plenty to enjoy. Being pre-menopausal or menopausal, natural lubrication may be diminishing. Worrabee Silk is the completely natural way to bring back the pleasure in sex.

Requirements
Must have
• Brandname: Worrabee Silk

Container Packaging specs: http://www.kelvorpackware-example.com/images/art/4871K07-C-FERN-RAISED.PDF
Dispenser: http://www.kelvorpackware-example.com/lotion-dispenser-pumps/p/kQT720R/
Should not have
• No post-coital pictures
No people
Nothing phallic

```html
<!DOCTYPE html>
<html lang="en">
<head>
<meta charset="utf-8">
<title>Worrabee Silk – Personal Lubricant Bottle</title>
<link rel="stylesheet" href="https://fonts.googleapis.com/css2?family=Great+Vibes&family=Montserrat:wght@400;600;700&family=Tinos:wght@700&display=swap">
<style>
  :root {
    --page: #ffffff;
    --cap: #1d1d1d;
    --cap-hi: #4a4a4a;
    --silver-dark: #6f6f6f;
    --silver-mid: #bdbdbd;
    --silver-light: #f7f7f4;
    --pink-deep: #a2439a;
    --pink-mid: #c987c2;
    --pink-light: #f3e3f1;
    --wine: #8a0f46;
    --leaf: #7bb63a;
    --leaf-light: #c5e08a;
    --bronze: #7a3b1e;
    --bronze-light: #d9a57c;
    --ink: #2a2020;
    --label-white: #ffffff;
  }
  html, body {
    margin: 0;
    padding: 0;
    width: 935px;
    height: 1200px;
    overflow: hidden;
    background: var(--page);
  }
  .canvas { display: block; width: 935px; height: 1200px; }
  .brand-word { font-family: "Montserrat", sans-serif; font-weight: 400; fill: var(--ink); }
  .title-script { font-family: "Great Vibes", cursive; }
  .title-script--front { fill: var(--leaf); }
  .title-script--back { fill: var(--ink); }
  .subtitle { font-family: "Montserrat", sans-serif; font-weight: 700; fill: var(--ink); }
  .small-print { font-family: "Montserrat", sans-serif; font-weight: 600; fill: var(--ink); }
  .feature-list { font-family: "Montserrat", sans-serif; font-weight: 400; fill: var(--ink); }
  .upc-label { font-family: "Tinos", serif; font-weight: 700; fill: #000; }
</style>
</head>
<body>
<svg class="canvas" viewBox="0 0 850 1090" xmlns="http://www.w3.org/2000/svg">
  <defs>
    <linearGradient id="silver" x1="0" x2="1" y1="0" y2="0">
      <stop offset="0" style="stop-color:var(--silver-dark)"/>
      <stop offset="0.25" style="stop-color:var(--silver-mid)"/>
      <stop offset="0.5" style="stop-color:var(--silver-light)"/>
      <stop offset="0.8" style="stop-color:var(--silver-mid)"/>
      <stop offset="1" style="stop-color:var(--silver-dark)"/>
    </linearGradient>
    <linearGradient id="pinkband" x1="0" x2="1" y1="0" y2="0">
      <stop offset="0" style="stop-color:var(--pink-deep)"/>
      <stop offset="0.3" style="stop-color:var(--pink-mid)"/>
      <stop offset="0.5" style="stop-color:var(--pink-light)"/>
      <stop offset="0.75" style="stop-color:var(--pink-mid)"/>
      <stop offset="1" style="stop-color:var(--pink-deep)"/>
    </linearGradient>
    <linearGradient id="capshade" x1="0" x2="1" y1="0" y2="0">
      <stop offset="0" style="stop-color:var(--cap)"/>
      <stop offset="0.45" style="stop-color:var(--cap-hi)"/>
      <stop offset="1" style="stop-color:var(--cap)"/>
    </linearGradient>
    <linearGradient id="bronze" x1="0" x2="1" y1="0" y2="0">
      <stop offset="0" style="stop-color:var(--bronze)"/>
      <stop offset="0.5" style="stop-color:var(--bronze-light)"/>
      <stop offset="1" style="stop-color:var(--bronze)"/>
    </linearGradient>

    <g id="bottle-shell">
      <!-- pump -->
      <path d="M 200 38 Q 210 30 240 32 L 330 40 Q 345 44 345 62 L 345 82 L 320 82 L 320 62 L 245 58 Q 210 56 200 60 Z" fill="url(#capshade)"/>
      <rect x="200" y="60" width="142" height="190" fill="url(#capshade)"/>
      <!-- neck band -->
      <rect x="200" y="248" width="142" height="90" fill="url(#pinkband)"/>
      <rect x="210" y="262" width="122" height="50" fill="url(#pinkband)" opacity="0.7" role="img" aria-label="Swirl ornament strip around the neck"/>
      <!-- body -->
      <path d="M 200 338 L 200 348 C 160 370 121 400 120 470 L 120 1062 Q 120 1080 140 1080 L 402 1080 Q 422 1080 422 1062 L 422 470 C 421 400 382 370 342 348 L 342 338 Z" fill="url(#silver)"/>
      <!-- lower patterned band -->
      <rect x="120" y="800" width="302" height="4" fill="var(--bronze-light)"/>
      <rect x="120" y="804" width="302" height="224" fill="url(#pinkband)" role="img" aria-label="Burgundy swirl pattern band"/>
      <rect x="120" y="1028" width="302" height="4" fill="var(--bronze-light)"/>
    </g>
  </defs>

  <!-- FRONT BOTTLE -->
  <g class="bottle bottle--front">
    <use href="#bottle-shell"/>
    <g class="logo">
      <circle cx="251" cy="414" r="15" fill="none" stroke="var(--ink)" stroke-width="2"/>
      <text class="brand-word" x="251" y="464" text-anchor="middle" font-size="22">worrabee</text>
    </g>
    <g class="front-label">
      <path d="M 120 495 Q 270 470 422 500 L 422 740 Q 270 770 120 740 Z" fill="url(#pinkband)"/>
      <path d="M 120 495 Q 270 470 422 500" fill="none" stroke="url(#bronze)" stroke-width="8"/>
      <path d="M 120 504 Q 270 478 422 508" fill="none" stroke="var(--leaf)" stroke-width="3"/>
      <path d="M 120 740 Q 270 770 422 740" fill="none" stroke="url(#bronze)" stroke-width="8"/>
      <path d="M 120 732 Q 270 760 422 732" fill="none" stroke="var(--leaf)" stroke-width="3"/>
      <circle cx="265" cy="620" r="108" fill="var(--pink-light)" opacity="0.35"/>
      <text class="title-script title-script--front" x="262" y="640" text-anchor="middle" font-size="60">Worrabee Silk</text>
      <text class="subtitle" x="264" y="660" text-anchor="middle" font-size="18">Personal Lubricant</text>
      <text class="small-print" x="262" y="694" text-anchor="middle" font-size="10">100% Pure Macadamia Oil</text>
      <text class="small-print" x="410" y="725" text-anchor="end" font-size="11">8oz</text>
    </g>
  </g>

  <!-- BACK BOTTLE -->
  <g class="bottle bottle--back" transform="translate(330 0)">
    <use href="#bottle-shell"/>
    <g class="back-label">
      <path d="M 120 495 Q 270 470 422 500 L 422 740 Q 270 770 120 740 Z" fill="url(#pinkband)"/>
      <path d="M 120 495 Q 270 470 422 500" fill="none" stroke="url(#bronze)" stroke-width="8"/>
      <path d="M 120 504 Q 270 478 422 508" fill="none" stroke="var(--leaf)" stroke-width="3"/>
      <path d="M 120 740 Q 270 770 422 740" fill="none" stroke="url(#bronze)" stroke-width="8"/>
      <path d="M 120 732 Q 270 760 422 732" fill="none" stroke="var(--leaf)" stroke-width="3"/>
      <text class="title-script title-script--back" x="200" y="546" text-anchor="middle" font-size="30">Worrabee Silk</text>
      <text class="feature-list" x="200" y="558" text-anchor="middle" font-size="9">Personal Lubricant</text>
      <g class="feature-list" font-size="9">
        <text x="145" y="574">- edible</text>
        <text x="145" y="584">- vegan</text>
        <text x="145" y="594">- gluten-free</text>
        <text x="145" y="604">- low allergen</text>
        <text x="145" y="614">- naturally anti-microbial</text>
        <text x="145" y="624">- anti-inflammatory</text>
      </g>
      <text class="small-print" x="215" y="640" text-anchor="middle" font-size="9">Ingredients:</text>
      <text class="small-print" x="215" y="656" text-anchor="middle" font-size="9">100% Macadamia Oil</text>
      <g class="logo">
        <circle cx="215" cy="682" r="12" fill="none" stroke="var(--ink)" stroke-width="2"/>
        <text class="brand-word" x="215" y="720" text-anchor="middle" font-size="18">worrabee</text>
      </g>
      <rect x="322" y="522" width="72" height="175" fill="var(--label-white)"/>
      <text class="upc-label" x="358" y="610" text-anchor="middle" font-size="30" transform="rotate(90 358 610)" dy="10">UPC</text>
    </g>
  </g>
</svg>
</body>
</html>
```